Hi Designers,

I will need 4 web pages designed. The web page looks like an App (if you click on the logo, or the icon on an iPad, it will take you to the website), but it is still a webpage.

Please check the attachment on this brief to understand what specific pages I need to be designed.

A .PSD (straight-up PhotoShop image) as final deliverable is fine, as long as you give us the exact “web color numbers”.

The design is for desktop and iPad but in a single unified web application, NOT separate web app and (native) iPad app.

Details:

Bright Harbor Policy Systems is developing a browser-based application for use on any mobile device or desktop. The app will be used by corporations to communicate with their employees regarding legal, regulatory and company requirements for conducting business. The app is known as “Workplace Guidance Hub.” When the user clicks on the icon for Workplace Guidance Hub, they will enter a site full of information that a company deems necessary for the employee to do his/her job. There are several content sections within the site, including a login page, training, policies, forms, news feeds and blogs.

The application has been built using Microsoft .NET, and fully supports CSS-type skinning; it uses traditional page layouts. We are seeking a product logo concept (image), a master application/desktop icon (image), as well as a full color scheme/theme/skin design for all areas of the application (header area, body text, menu bar, etc.) in the form of a CSS. The look should be clean, crisp and professional; nothing cartoony or whimsical. It should be easy to read and “airy”.

We have sketched prototypes for the basic application page layout that we can send as a next step of the process.
Updates

Screen shots have been uploaded to this project.  Please use them to guide your design.

Dear designers,

I apologize for the delay in providing feedback. My partners and I will provide feedback in a few days. Thank you for your patience.

Industry/Entity Type

Business

Font styles to use
Other font styles liked:
• see font on screen shots when uploaded

```html
<!DOCTYPE html>
<html lang="en">
<head>
<meta charset="utf-8">
<title>Workplace Guidance Hub – Dashboard</title>
<link href="https://fonts.googleapis.com/css2?family=Signika:wght@300;400;600&display=swap" rel="stylesheet">
<style>
:root{
  --page-bg:#f2eded;
  --app-bg:#ececec;
  --panel:#ffffff;
  --panel-soft:#f7f7f7;
  --nav-bg:#e3e3e3;
  --nav-line:#d2d2d2;
  --icon-grey:#8c8c8c;
  --text:#6f6f6f;
  --text-dark:#555555;
  --heading-grey:#a8a8a8;
  --coral:#ff6a62;
  --teal:#5cdcc1;
  --teal-text:#2fbf9f;
  --sky:#5ec8f1;
  --sky-icon:#4bb9e8;
  --link:#2a8fc4;
  --badge:#f03a2e;
  --lb-head:#9d9d9d;
  --lb-row-a:#d0d0d0;
  --lb-row-b:#bfbfbf;
  --photo-a:#b8b3ad;
  --photo-b:#8c8680;
}
*{box-sizing:border-box;margin:0;padding:0}
html,body{width:1200px;height:994px;overflow:hidden}
body{background:var(--page-bg);font-family:'Signika',Arial,sans-serif;color:var(--text)}
.app{position:absolute;left:0;top:47px;width:1200px;height:900px;background:var(--app-bg);overflow:hidden}

/* top navigation */
.topbar{height:63px;background:var(--nav-bg);display:flex;border-bottom:1px solid var(--nav-line)}
.nav-tab{width:139px;display:flex;align-items:center;justify-content:center;border-right:1px solid var(--nav-line);position:relative}
.nav-tab svg{width:38px;height:38px}
.badge{position:absolute;left:78px;top:13px;background:var(--badge);color:#fff;font-size:12px;font-weight:600;width:18px;height:18px;border-radius:3px;text-align:center;line-height:18px}
.user{margin-left:auto;display:flex;align-items:center;gap:22px;padding-right:46px;font-size:16px;color:var(--text)}
.user-photo{width:40px;height:40px;background:linear-gradient(160deg,#d8d2cc,#a39e98)}
.caret{width:0;height:0;border-left:6px solid transparent;border-right:6px solid transparent;border-top:7px solid var(--icon-grey)}

.columns{display:flex;height:837px}

/* industry news */
.news{width:241px;background:var(--panel)}
.col-head{height:40px;margin-top:8px;display:flex;align-items:center;gap:10px;padding-left:14px;color:#fff;font-size:17px;font-weight:600}
.news .col-head{background:var(--heading-grey)}
.col-head svg{width:20px;height:20px}
.search{margin:12px 9px 14px;height:29px;border:1px solid #c9c9c9;border-radius:3px;display:flex;align-items:center;gap:10px;padding-left:12px;font-size:12px;color:#a5a5a5}
.search svg{width:13px;height:13px}
.news-item{height:156px;display:flex;gap:22px;padding:15px 12px 0 14px;position:relative}
.news-item:nth-child(even){background:var(--panel-soft)}
.news-item.active::before{content:"";position:absolute;left:0;top:0;bottom:0;width:4px;background:var(--coral)}
.date{width:28px;text-align:center;font-size:11px;color:var(--text)}
.date-box{width:28px;height:26px;border:2px solid #9a9a9a;border-top-width:5px;border-radius:2px;font-size:12px;line-height:18px;margin-bottom:2px}
.news-body{font-size:12.5px;line-height:16px;color:var(--text-dark)}
.news-body a{display:block;margin-top:16px;color:var(--link);text-decoration:underline;font-size:12.5px}

/* centre */
.centre{width:706px;padding:8px 10px 0}
.welcome-head{height:38px;background:var(--coral);color:#fff;font-size:17px;font-weight:600;display:flex;align-items:center;gap:12px;padding-left:22px;margin:0 0 0 0}
.welcome-head svg{width:18px;height:18px}
.welcome-body{background:var(--panel);height:114px;display:flex;gap:26px;padding:12px 20px}
.welcome-photo{width:93px;height:87px;flex:none;background:linear-gradient(150deg,#e7d7b8,#8a7a69)}
.welcome-body p{font-size:13.5px;line-height:18px;color:var(--text-dark);padding-top:10px}
.split{display:flex;gap:15px;margin-top:14px}
.whatsnew{width:332px;background:var(--panel);height:656px;margin-left:4px}
.whatsnew .col-head,.game .col-head{margin-top:0;height:38px;padding-left:18px;font-weight:600}
.whatsnew .col-head{background:var(--teal)}
.game .col-head{background:var(--sky)}
.update{margin:0 17px;height:92px;border-bottom:1px solid #e1e1e1;display:flex;gap:17px;align-items:center}
.update:first-of-type{margin-top:8px}
.update-thumb{width:58px;height:44px;flex:none;background:linear-gradient(150deg,var(--photo-a),var(--photo-b))}
.update-date{font-size:13.5px;color:var(--teal-text);margin-bottom:3px}
.update p{font-size:12.5px;line-height:16px;color:var(--text)}
.game{width:329px;background:var(--panel);height:656px}
.card{margin:10px 10px 0;height:135px;background:var(--panel-soft);border-bottom:5px solid #cfcfcf;display:flex;gap:34px;padding:22px 20px 0 24px}
.card + .card{margin-top:16px}
.card svg{width:40px;height:40px;flex:none;margin-top:-2px}
.card h3{font-size:17px;font-weight:400;color:var(--text-dark);margin-bottom:10px}
.card p{font-size:12.5px;line-height:16px;color:var(--text)}

/* leaderboard */
.board{width:253px;background:var(--lb-row-b)}
.board .col-head{background:var(--lb-head);padding-left:38px}
.board table{width:100%;border-collapse:collapse;font-size:12.5px;color:var(--text-dark)}
.board th{height:40px;font-weight:400;font-size:12px;color:var(--text);background:var(--app-bg);text-align:left}
.board td{height:31.5px}
.board tr.first td{height:48px;background:var(--app-bg)}
.board tbody tr:nth-child(even){background:var(--lb-row-a)}
.board tbody tr:nth-child(odd){background:var(--lb-row-b)}
.c-rank{width:48px;padding-left:15px}
.c-player{width:100px}
.c-pct{width:56px}
.rank{display:inline-block;width:15px;height:15px;border-radius:50%;background:#ececec;border:1px solid #b5b5b5;font-size:9px;line-height:13px;text-align:center}
.first .rank{border-radius:2px}
</style>
</head>
<body>
<div class="app">
  <header class="topbar">
    <div class="nav-tab">
      <svg viewBox="0 0 40 40" fill="none" stroke="var(--icon-grey)" stroke-width="3"><path d="M5 20 20 7l15 13"/><path d="M10 17v16h20V17"/></svg>
      <span class="badge">5</span>
    </div>
    <div class="nav-tab">
      <svg viewBox="0 0 40 40" fill="none" stroke="var(--icon-grey)" stroke-width="2.5"><rect x="5" y="7" width="26" height="27" rx="1"/><path d="M10 14h6M10 20h12M10 26h10"/><path d="M24 30l10-12 3 3-10 12h-3z" fill="var(--icon-grey)"/></svg>
    </div>
    <div class="nav-tab">
      <svg viewBox="0 0 40 40" fill="var(--icon-grey)"><rect x="4" y="7" width="32" height="21" rx="1"/><rect x="17" y="28" width="6" height="4"/><rect x="12" y="32" width="16" height="3"/></svg>
    </div>
    <div class="nav-tab">
      <svg viewBox="0 0 40 40" fill="none" stroke="var(--icon-grey)" stroke-width="4"><path d="M30 14a11 11 0 0 0-20 3"/><path d="M10 26a11 11 0 0 0 20-3"/><path d="M24 14h8V6" stroke-width="3"/><path d="M16 26H8v8" stroke-width="3"/></svg>
    </div>
    <div class="user">
      <div class="user-photo" role="img" aria-label="User profile photo"></div>
      <span>Daniel Whitford</span>
      <span class="caret"></span>
    </div>
  </header>

  <div class="columns">
    <aside class="news">
      <div class="col-head">
        <svg viewBox="0 0 20 20" fill="none" stroke="#fff" stroke-width="2"><rect x="2" y="4" width="13" height="14"/><path d="M9 11l8-8" /></svg>
        Industry news
      </div>
      <div class="search">
        <svg viewBox="0 0 14 14" fill="none" stroke="#9a9a9a" stroke-width="2"><circle cx="6" cy="6" r="4.5"/><path d="M9.5 9.5 13 13"/></svg>
        Search news...
      </div>
      <div class="news-list">
        <article class="news-item">
          <div class="date"><div class="date-box">28</div>oct</div>
          <div class="news-body">Lorem ipsum dolor sit amet, ad ius inani vocibus. An nam possim fastidii, usu in fuisset dissentias, nec at persius denique<a href="#">monthly report major's office</a></div>
        </article>
        <article class="news-item active">
          <div class="date"><div class="date-box">28</div>oct</div>
          <div class="news-body">Lorem ipsum dolor sit amet, ad ius inani vocibus. An nam possim fastidii, usu in fuisset dissentias, nec at persius denique<a href="#">monthly report major's office</a></div>
        </article>
        <article class="news-item">
          <div class="date"><div class="date-box">28</div>oct</div>
          <div class="news-body">Lorem ipsum dolor sit amet, ad ius inani vocibus. An nam possim fastidii, usu in fuisset dissentias, nec at persius denique<a href="#">monthly report major's office</a></div>
        </article>
        <article class="news-item">
          <div class="date"><div class="date-box">28</div>oct</div>
          <div class="news-body">Lorem ipsum dolor sit amet, ad ius inani vocibus. An nam possim fastidii, usu in fuisset dissentias, nec at persius denique<a href="#">monthly report major's office</a></div>
        </article>
      </div>
    </aside>

    <main class="centre">
      <section class="welcome">
        <div class="welcome-head">
          <svg viewBox="0 0 20 20" fill="#fff"><path d="M10 1l2.7 6 6.3.6-4.8 4.3 1.4 6.3L10 15l-5.6 3.2 1.4-6.3L1 7.6l6.3-.6z"/></svg>
          Welcome to workplace guidance hub
        </div>
        <div class="welcome-body">
          <div class="welcome-photo" role="img" aria-label="Photo of a smiling colleague"></div>
          <p>Lorem ipsum dolor sit amet, eu vix summo primis qualisque. Usu nihil labitur atomorum eu, pri quod modo nemore cu, cu graeco perfecto vis. Ex est idque facilisis, alia intellegebat ius an, his te duis maiorum moderatius. Delicata necessitatibus mei in, mel</p>
        </div>
      </section>

      <div class="split">
        <section class="whatsnew">
          <div class="col-head">
            <svg viewBox="0 0 20 20" fill="#fff"><path d="M10 3c4.4 0 8 2.7 8 6s-3.6 6-8 6l-5 3 1-4C3.5 13 2 11.2 2 9c0-3.3 3.6-6 8-6z"/></svg>
            What's new
          </div>
          <article class="update"><div class="update-thumb" role="img" aria-label="Photo of a man on the phone at his desk"></div><div><div class="update-date">11/11/2013</div><p>Prompta civibus gloriatur mea te, an cum facete suavitate, ei vim corrumpit</p></div></article>
          <article class="update"><div class="update-thumb" role="img" aria-label="Photo of a man on the phone at his desk"></div><div><div class="update-date">11/11/2013</div><p>Prompta civibus gloriatur mea te, an cum facete suavitate, ei vim corrumpit</p></div></article>
          <article class="update"><div class="update-thumb" role="img" aria-label="Photo of a man on the phone at his desk"></div><div><div class="update-date">11/11/2013</div><p>Prompta civibus gloriatur mea te, an cum facete suavitate, ei vim corrumpit</p></div></article>
          <article class="update"><div class="update-thumb" role="img" aria-label="Photo of a man on the phone at his desk"></div><div><div class="update-date">11/11/2013</div><p>Prompta civibus gloriatur mea te, an cum facete suavitate, ei vim corrumpit</p></div></article>
          <article class="update"><div class="update-thumb" role="img" aria-label="Photo of a man on the phone at his desk"></div><div><div class="update-date">11/11/2013</div><p>Prompta civibus gloriatur mea te, an cum facete suavitate, ei vim corrumpit</p></div></article>
          <article class="update"><div class="update-thumb" role="img" aria-label="Photo of a man on the phone at his desk"></div><div><div class="update-date">11/11/2013</div><p>Prompta civibus gloriatur mea te, an cum facete suavitate, ei vim corrumpit</p></div></article>
        </section>

        <section class="game">
          <div class="col-head">
            <svg viewBox="0 0 20 20" fill="#fff"><circle cx="10" cy="6" r="4"/><path d="M2 18c0-4 3.6-6 8-6s8 2 8 6z"/></svg>
            Compliance game center
          </div>
          <div class="card">
            <svg viewBox="0 0 40 40" fill="none" stroke="var(--sky-icon)" stroke-width="3"><path d="M8 24v-6a12 12 0 0 1 24 0v6"/><rect x="6" y="21" width="6" height="9" rx="2" fill="var(--sky-icon)"/><rect x="28" y="21" width="6" height="9" rx="2" fill="var(--sky-icon)"/><path d="M31 30c0 4-4 5-9 5"/></svg>
            <div><h3>Use Preferances</h3><p>Lorem ipsum dolor sit amet, ad ius inani vocibus. An nam possim fastidii, usu in fuisset dissentias,</p></div>
          </div>
          <div class="card">
            <svg viewBox="0 0 40 40" fill="none" stroke="var(--sky-icon)" stroke-width="3"><rect x="4" y="6" width="32" height="22"/><path d="M10 13h14M10 19h10"/><path d="M22 34l10-10 3 3-10 10h-3z" fill="var(--sky-icon)"/></svg>
            <div><h3>Real Time Updates</h3><p>Lorem ipsum dolor sit amet, ad ius inani vocibus. An nam possim fastidii, usu in fuisset dissentias,</p></div>
          </div>
          <div class="card">
            <svg viewBox="0 0 40 40" fill="none" stroke="var(--sky-icon)" stroke-width="3"><rect x="7" y="4" width="26" height="32" rx="2"/><path d="M12 12h2M18 12h10M12 20h2M18 20h10M12 28h2M18 28h10"/></svg>
            <div><h3>Team Standings</h3><p>Lorem ipsum dolor sit amet, ad ius inani vocibus. An nam possim fastidii, usu in fuisset dissentias,</p></div>
          </div>
          <div class="card">
            <svg viewBox="0 0 40 40" fill="none" stroke="var(--sky-icon)" stroke-width="3"><path d="M14 26c0-5-4-6-4-11a10 10 0 0 1 20 0c0 5-4 6-4 11z" fill="var(--sky-icon)"/><path d="M15 31h10M17 35h6M20 0v2M3 15h3M34 15h3M7 4l2 2M33 4l-2 2"/></svg>
            <div><h3>Earn Bonus Points</h3><p>Lorem ipsum dolor sit amet, ad ius inani vocibus. An nam possim fastidii, usu in fuisset dissentias,</p></div>
          </div>
        </section>
      </div>
    </main>

    <aside class="board">
      <div class="col-head">Leaderboard</div>
      <table>
        <thead><tr><th class="c-rank">rank</th><th class="c-player">player</th><th class="c-pct">%</th><th>score</th></tr></thead>
        <tbody>
          <tr class="first"><td class="c-rank"><span class="rank">1</span></td><td>Marcus, L</td><td>92%</td><td>5093</td></tr>
          <tr><td class="c-rank"><span class="rank">2</span></td><td>Andrea,D</td><td>91%</td><td>5029</td></tr>
          <tr><td class="c-rank"><span class="rank">3</span></td><td>Marcus, L</td><td>92%</td><td>5093</td></tr>
          <tr><td class="c-rank"><span class="rank">2</span></td><td>Andrea,D</td><td>91%</td><td>5029</td></tr>
          <tr><td class="c-rank"><span class="rank">3</span></td><td>Marcus, L</td><td>92%</td><td>5093</td></tr>
          <tr><td class="c-rank"><span class="rank">3</span></td><td>Marcus, L</td><td>92%</td><td>5093</td></tr>
          <tr><td class="c-rank"><span class="rank">2</span></td><td>Andrea,D</td><td>91%</td><td>5029</td></tr>
          <tr><td class="c-rank"><span class="rank">2</span></td><td>Andrea,D</td><td>91%</td><td>5029</td></tr>
          <tr><td class="c-rank"><span class="rank">2</span></td><td>Andrea,D</td><td>91%</td><td>5029</td></tr>
          <tr><td class="c-rank"><span class="rank">3</span></td><td>Marcus, L</td><td>92%</td><td>5093</td></tr>
          <tr><td class="c-rank"><span class="rank">3</span></td><td>Marcus, L</td><td>92%</td><td>5093</td></tr>
          <tr><td class="c-rank"><span class="rank">2</span></td><td>Andrea,D</td><td>91%</td><td>5029</td></tr>
          <tr><td class="c-rank"><span class="rank">2</span></td><td>Andrea,D</td><td>91%</td><td>5029</td></tr>
          <tr><td class="c-rank"><span class="rank">3</span></td><td>Marcus, L</td><td>92%</td><td>5093</td></tr>
          <tr><td class="c-rank"><span class="rank">2</span></td><td>Andrea,D</td><td>91%</td><td>5029</td></tr>
          <tr><td class="c-rank"><span class="rank">3</span></td><td>Marcus, L</td><td>92%</td><td>5093</td></tr>
          <tr><td class="c-rank"><span class="rank">2</span></td><td>Andrea,D</td><td>91%</td><td>5029</td></tr>
          <tr><td class="c-rank"><span class="rank">3</span></td><td>Marcus, L</td><td>92%</td><td>5093</td></tr>
          <tr><td class="c-rank"><span class="rank">2</span></td><td>Andrea,D</td><td>91%</td><td>5029</td></tr>
          <tr><td class="c-rank"><span class="rank">3</span></td><td>Marcus, L</td><td>92%</td><td>5093</td></tr>
          <tr><td class="c-rank"><span class="rank">3</span></td><td>Marcus, L</td><td>92%</td><td>5093</td></tr>
          <tr><td class="c-rank"><span class="rank">3</span></td><td>Marcus, L</td><td>92%</td><td>5093</td></tr>
          <tr><td class="c-rank"><span class="rank">3</span></td><td>Marcus, L</td><td>92%</td><td>5093</td></tr>
        </tbody>
      </table>
    </aside>
  </div>
</div>
</body>
</html>
```